Complete Banner Set For Web Display Ads - Including Zimbly

Ads are driving to a free web class on real estate investing made easy. The offer is for software and training that solves their number 1 challenge - Finding Deals.
Examples of copy suggestions and offer....
"Invest In Real Estate Like A Pro"
"Access Never Before Seen Inventory In Seconds"
"The Country's Best Source For Off-Market Deals"
Brody Halvaney "#1 Real Estate Investing Strategy"
Real Estate

```html
<!DOCTYPE html>
<html lang="en">
<head>
<meta charset="utf-8">
<title>Invest In Real Estate Like A Pro – Display Banners</title>
<link rel="stylesheet" href="https://fonts.googleapis.com/css2?family=Open+Sans:wght@700;800&display=swap">
<style>
  :root {
    --canvas: #ffffff;
    --white: #ffffff;
    --green: #8dc63f;
    --orange: #f7941d;
    --ink-dark: #2b2118;
    --ink-olive: #55641f;
  }
  html, body {
    margin: 0;
    padding: 0;
    width: 1200px;
    height: 1200px;
    overflow: hidden;
    background: var(--canvas);
  }
  .canvas {
    position: relative;
    width: 1200px;
    height: 1200px;
    font-family: "Open Sans", Arial, sans-serif;
  }
  .banner {
    position: absolute;
    width: 360px;
    height: 300px;
    overflow: hidden;
  }
  .banner--warm   { left: 187px; top: 287px; }
  .banner--green  { left: 187px; top: 659px; }
  .banner--blend  { left: 653px; top: 437px; }

  .banner__photo {
    position: absolute;
    inset: 0;
  }
  .banner--warm .banner__photo {
    background:
      radial-gradient(ellipse 110px 150px at 290px 140px, rgba(214,150,110,.85), rgba(214,150,110,0) 70%),
      linear-gradient(90deg, #7c5a44 0%, #6a4a32 35%, #9a6a3c 65%, #d8892e 100%);
  }
  .banner--green .banner__photo {
    background:
      radial-gradient(ellipse 110px 150px at 290px 140px, rgba(200,160,135,.8), rgba(200,160,135,0) 70%),
      linear-gradient(90deg, #8dbf3a 0%, #6f9a2e 30%, #55603a 60%, #3f4346 100%);
  }
  .banner--blend .banner__photo {
    background:
      radial-gradient(ellipse 110px 150px at 290px 140px, rgba(220,150,95,.8), rgba(220,150,95,0) 70%),
      linear-gradient(90deg, #8cc23c 0%, #7a9c34 35%, #a7863a 65%, #e08e2a 100%);
  }

  .banner__headline {
    position: absolute;
    left: 34px;
    top: 34px;
    margin: 0;
    font-weight: 700;
    font-size: 29px;
    line-height: 42px;
    color: var(--white);
    letter-spacing: -0.2px;
  }
  .banner__headline span { display: block; }
  .accent-green { color: var(--green); }
  .accent-orange { color: var(--orange); }
  .accent-boxed {
    background: var(--white);
    padding: 0 2px;
  }

  .banner__cta {
    position: absolute;
    left: 34px;
    top: 223px;
    width: 149px;
    height: 50px;
    border-radius: 6px;
    background: var(--white);
    display: flex;
    align-items: center;
    justify-content: center;
    font-weight: 700;
    font-size: 19px;
    color: var(--ink-olive);
    text-decoration: none;
  }
  .banner--warm .banner__cta { color: var(--ink-dark); }
</style>
</head>
<body>
<main class="canvas">

  <section class="banner banner--warm">
    <div class="banner__photo" role="img" aria-label="Portrait of a bald man in a grey blazer seated on outdoor steps, warm orange tint"></div>
    <h2 class="banner__headline">
      <span>Invest In</span>
      <span>Real Estate</span>
      <span><span class="accent-green" style="display:inline">Like</span> A <span class="accent-orange" style="display:inline">Pro</span></span>
    </h2>
    <a class="banner__cta" href="#">CLICK NOW</a>
  </section>

  <section class="banner banner--green">
    <div class="banner__photo" role="img" aria-label="Portrait of a bald man in a grey blazer seated on outdoor steps, green tint"></div>
    <h2 class="banner__headline">
      <span>Invest In</span>
      <span>Real Estate</span>
      <span><span class="accent-green accent-boxed" style="display:inline">Like</span> A <span class="accent-orange" style="display:inline">Pro</span></span>
    </h2>
    <a class="banner__cta" href="#">CLICK NOW</a>
  </section>

  <section class="banner banner--blend">
    <div class="banner__photo" role="img" aria-label="Portrait of a bald man in a grey blazer seated on outdoor steps, green to orange tint"></div>
    <h2 class="banner__headline">
      <span>Invest In</span>
      <span>Real Estate</span>
      <span><span class="accent-green accent-boxed" style="display:inline">Like</span> A <span class="accent-orange accent-boxed" style="display:inline">Pro</span></span>
    </h2>
    <a class="banner__cta" href="#">CLICK NOW</a>
  </section>

</main>
</body>
</html>
```